We need to have 2 different retractable banners designed that will be used at a variety of events. We plan to have the banners printed through printbriskly.example. According to their site, specs are as follows: Retractable banners are digitally printed on 12oz double-sided smooth vinyl. While the area on the retractable banners is 33 x 78, the customer will want to provide a file that has an area of 35 x 82 to account for bleed, with 3" of that vertical bleed at the bottom of the design. Recommneded DPI is 150. Upload capacity for retractable banners is 100MP.

Banner #1: Cascadia Labor Alliance logo at top; then the following text placed lower on the banner: Providing leadership that promotes and advances Oregon's workforce system. At the bottom of banner: cascadialabor alliance.example

Banner #2: Cascadia Labor Alliance logo at top; then the following text placed lower on the banner: Oregon's workforce system ensures all Oregonians possess the talent needed for communities to thrive and prosper. At the bottom of banner: cascadialaboralliance.example

Color scheme: complimentary colors of the Cascadia Labor Alliance logo.
Images: images representative of Oregon (for example: map of Oregon, Douglas fir trees, coastal range, etc.

I've attached a couple of previous banners created as a reference.

```html
<!DOCTYPE html>
<html lang="en">
<head>
<meta charset="utf-8">
<title>Cascadia Labor Alliance – Retractable Banners</title>
<link rel="stylesheet" href="https://fonts.googleapis.com/css2?family=Raleway:wght@300;500;800&family=Roboto:wght@400&display=swap">
<style>
  :root {
    --backdrop: #4dd4f0;
    --navy: #0b2d6e;
    --magenta: #9b0650;
    --plum: #6a0338;
    --paper: #efefef;
    --white: #ffffff;
  }
  * { margin: 0; padding: 0; box-sizing: border-box; }
  html, body { width: 1200px; height: 1200px; overflow: hidden; }
  body { background: var(--backdrop); position: relative; font-family: "Raleway", sans-serif; }
  .banner { position: absolute; top: 80px; width: 410px; height: 1002px; box-shadow: 0 6px 18px rgba(0,0,0,.18); }
  .banner--coast { left: 142px; }
  .banner--forest { left: 648px; }
  .banner svg { display: block; width: 100%; height: 100%; }
  .brand-name { font-family: "Raleway", sans-serif; font-weight: 500; font-size: 19px; letter-spacing: 3px; fill: var(--navy); }
  .tagline { font-family: "Raleway", sans-serif; font-size: 33px; fill: var(--white); }
  .tagline--long { font-size: 28px; }
  .tagline .light { font-weight: 300; }
  .tagline .strong { font-weight: 800; }
  .web-address { font-family: "Roboto", sans-serif; font-size: 20px; fill: var(--white); }
  .rule { stroke: var(--white); stroke-width: 2; }
</style>
</head>
<body>

<div class="banner banner--coast">
  <svg viewBox="0 0 512 1252" xmlns="http://www.w3.org/2000/svg">
    <defs>
      <linearGradient id="coast-fill" x1="0" y1="0" x2="0" y2="1">
        <stop offset="0" stop-color="#cfe0e8"/>
        <stop offset="0.35" stop-color="#8a9a6a"/>
        <stop offset="0.6" stop-color="#b8a890"/>
        <stop offset="0.8" stop-color="#2ec4e0"/>
        <stop offset="1" stop-color="#1a9cc0"/>
      </linearGradient>
    </defs>
    <rect class="field" width="512" height="1252" fill="var(--navy)"/>
    <polygon class="header-panel" points="0,0 512,0 512,190 0,320" fill="var(--paper)"/>
    <polygon class="photo-area" role="img" aria-label="Coastal cliffs above a turquoise cove" points="0,352 512,250 512,624 0,742" fill="url(#coast-fill)"/>
    <polygon class="accent-corner" points="350,255 512,190 512,288" fill="var(--magenta)"/>
    <polygon class="accent-band" points="0,742 512,624 512,687 0,817" fill="var(--magenta)"/>
    <polygon class="accent-shade" points="0,727 170,755 0,817" fill="var(--plum)"/>
    <rect class="brand-mark" x="200" y="48" width="112" height="112" rx="12" fill="var(--navy)"/>
    <text class="brand-name" x="256" y="198" text-anchor="middle">CASCADIA LABOR</text>
    <text class="brand-name" x="256" y="222" text-anchor="middle">ALLIANCE</text>
    <text class="tagline" x="48" y="878"><tspan class="light">PROVIDING </tspan><tspan class="strong">LEADERSHIP</tspan></text>
    <text class="tagline" x="50" y="930"><tspan class="light">THAT </tspan><tspan class="strong">PROMOTES AND</tspan></text>
    <text class="tagline" x="50" y="982"><tspan class="strong">ADVANCES </tspan><tspan class="light">OREGON’S</tspan></text>
    <text class="tagline" x="50" y="1034"><tspan class="light">WORKFORCE SYSTEM.</tspan></text>
    <line class="rule" x1="0" y1="1195" x2="86" y2="1195"/>
    <text class="web-address" x="256" y="1202" text-anchor="middle">cascadialaboralliance.example</text>
    <line class="rule" x1="424" y1="1195" x2="512" y2="1195"/>
  </svg>
</div>

<div class="banner banner--forest">
  <svg viewBox="0 0 512 1252" xmlns="http://www.w3.org/2000/svg">
    <defs>
      <linearGradient id="forest-fill" x1="0" y1="0" x2="1" y2="1">
        <stop offset="0" stop-color="#3f7a2e"/>
        <stop offset="0.45" stop-color="#2d5e22"/>
        <stop offset="0.55" stop-color="#8a7a3a"/>
        <stop offset="1" stop-color="#4e8a34"/>
      </linearGradient>
    </defs>
    <rect class="field" width="512" height="1252" fill="var(--magenta)"/>
    <polygon class="header-panel" points="0,0 512,0 512,190 0,320" fill="var(--paper)"/>
    <polygon class="accent-band-top" points="0,320 512,190 512,260 0,380" fill="var(--navy)"/>
    <polygon class="photo-area" role="img" aria-label="Douglas fir branch with a hanging cone" points="0,380 512,252 512,624 0,742" fill="url(#forest-fill)"/>
    <polygon class="accent-corner" points="350,255 512,190 512,288" fill="var(--magenta)"/>
    <polygon class="accent-band" points="0,742 512,624 512,687 0,817" fill="var(--navy)"/>
    <polygon class="accent-shade" points="0,727 170,755 0,817" fill="var(--plum)"/>
    <rect class="brand-mark" x="200" y="48" width="112" height="112" rx="12" fill="var(--navy)"/>
    <text class="brand-name" x="256" y="198" text-anchor="middle">CASCADIA LABOR</text>
    <text class="brand-name" x="256" y="222" text-anchor="middle">ALLIANCE</text>
    <text class="tagline tagline--long" x="48" y="870"><tspan class="light">OREGON’S WORKFORCE</tspan></text>
    <text class="tagline tagline--long" x="48" y="918"><tspan class="light">SYSTEM </tspan><tspan class="strong">ENSURES ALL</tspan></text>
    <text class="tagline tagline--long" x="48" y="966"><tspan class="strong">OREGONIANS </tspan><tspan class="light">POSSESS</tspan></text>
    <text class="tagline tagline--long" x="48" y="1014"><tspan class="light">THE </tspan><tspan class="strong">TALENT </tspan><tspan class="light">NEEDED</tspan></text>
    <text class="tagline tagline--long" x="48" y="1062"><tspan class="light">FOR </tspan><tspan class="strong">COMMUNITIES </tspan><tspan class="light">TO</tspan></text>
    <text class="tagline tagline--long" x="48" y="1110"><tspan class="strong">THRIVE </tspan><tspan class="light">AND </tspan><tspan class="strong">PROSPER.</tspan></text>
    <line class="rule" x1="0" y1="1195" x2="86" y2="1195"/>
    <text class="web-address" x="256" y="1202" text-anchor="middle">cascadialaboralliance.example</text>
    <line class="rule" x1="424" y1="1195" x2="512" y2="1195"/>
  </svg>
</div>

</body>
</html>
```